Wordpress template re-design of current website

We need a WordPress template design and new look for our existing website. Our existing site it located at www.velmoro.com.au We are a tech company and want a fresh, clean modern website that matches our brand, services and logo colors. Our main Services are hospitality solutions, Velmoro TV solution and managed networks, more information on these can come from our existing website.

Target Market(s)

We are a tech company so must have a modern feel for new technology

Industry/Entity Type

It Company

Number of Pages Required

5+ page

Font styles to use
Sans Serif

Requirements
Must have
• Be based on a wordpress templete design and match the services that we have in our existing website, in the testimonials want a place for video testimonials as well as text. Nice clean icons used for graphics to represent services.
Nice to have
• nice visual representation of our services in the way of clean icons etc
Should not have
• Clutter

```html
<!DOCTYPE html>
<html lang="en">
<head>
<meta charset="utf-8">
<title>Velmoro Wireless Internet</title>
<link href="https://fonts.googleapis.com/css2?family=Exo+2:ital,wght@0,500;0,600;0,700;1,500;1,600;1,700&family=Lato:ital,wght@0,400;0,700;1,400;1,700&display=swap" rel="stylesheet">
<style>
:root{
  --blue:#0b4a92;
  --blue-dark:#083a74;
  --blue-deep:#06305f;
  --grey-icon:#6d747c;
  --grey-btn:#6f767d;
  --text:#222;
  --muted:#555;
  --light:#f1f2f3;
  --dark:#2b2b2b;
  --white:#fff;
}
*{margin:0;padding:0;box-sizing:border-box}
html,body{width:1200px;height:3502px;overflow:hidden;background:#fff}
body{font-family:"Lato",sans-serif;color:var(--text);position:relative}
.page{position:relative;width:1200px;height:3502px;overflow:hidden}
.abs{position:absolute}
.head{font-family:"Exo 2",sans-serif;font-style:italic;font-weight:700}
.btn{position:absolute;background:var(--grey-btn);color:#fff;font-family:"Exo 2",sans-serif;font-style:italic;font-weight:600;font-size:17px;border-radius:22px;text-align:center;line-height:38px;height:38px}

/* header */
.site-header{left:0;top:0;width:1200px;height:105px;background:#fff}
.brand{left:78px;top:26px;display:flex;align-items:center;gap:12px}
.brand-name{font-family:"Exo 2",sans-serif;font-weight:700;font-size:44px;color:var(--blue);line-height:1}
.brand-dot{width:22px;height:22px;border-radius:50%;background:var(--blue)}
.top-contact{right:80px;top:8px;display:flex;align-items:center;gap:10px;font-size:16px;color:#333}
.social{width:26px;height:26px;border:2px solid #8da9c9;border-radius:50%}
.main-nav{left:446px;top:61px;display:flex;align-items:center;font-family:"Exo 2",sans-serif;font-size:15px;font-weight:500;color:#333}
.main-nav a{color:inherit;text-decoration:none;padding:6px 18px;margin-right:14px}
.main-nav .current{background:var(--blue);color:#fff;border-radius:14px;font-weight:600}
.portal{left:1022px;top:59px;width:98px;height:30px;background:var(--blue);color:#fff;font-family:"Exo 2",sans-serif;font-weight:700;font-size:14px;text-align:center;line-height:30px;border-radius:3px}

/* hero */
.hero{left:0;top:105px;width:1200px;height:463px;background:linear-gradient(100deg,#2b1d12 0%,#6b4a2c 28%,#3b3a45 55%,#1d2a44 75%,#5a3f2a 100%)}
.hero-title{left:0;top:192px;width:1200px;text-align:center;color:#fff;font-family:"Exo 2",sans-serif;font-weight:600;font-size:46px;text-shadow:0 2px 6px rgba(0,0,0,.5)}
.hero-btn{left:536px;top:267px;width:128px;height:40px;background:var(--blue);color:#fff;border-radius:20px;font-family:"Exo 2",sans-serif;font-weight:600;font-size:17px;text-align:center;line-height:40px}
.hero-tab{left:546px;top:434px;width:108px;height:29px;background:#f1f2f3;border-radius:10px 10px 0 0;display:flex;justify-content:center;align-items:center;gap:6px}
.hero-tab i{width:13px;height:13px;border-radius:50%;background:#555;display:block}
.hero-tab i.on{background:#fff;border:2px solid #555}

/* services */
.services{left:0;top:568px;width:1200px;height:737px;background:var(--light)}
.section-title{left:0;width:1200px;text-align:center;font-size:42px;color:var(--blue)}
.services-lead{left:0;top:96px;width:1200px;text-align:center;font-size:13px;color:#333}
.svc-label{font-family:"Exo 2",sans-serif;font-style:italic;font-weight:500;font-size:19px;color:#555;text-align:center;width:260px;letter-spacing:.5px}
.svc-label.active{color:var(--blue);font-weight:600}
.svc-icon{width:108px;height:108px;border-radius:50%;background:var(--grey-icon);border:5px solid #fff;box-shadow:0 2px 6px rgba(0,0,0,.25);display:flex;align-items:center;justify-content:center}
.svc-icon.active{background:var(--blue)}
.hub{left:400px;top:376px;width:400px;height:400px;border-radius:50%;background:#fff;border:14px solid #e4e5e7;display:flex;align-items:center;justify-content:center;flex-direction:column}
.hub-name{font-family:"Exo 2",sans-serif;font-weight:700;font-size:66px;color:var(--blue);display:flex;align-items:center;gap:14px;margin-top:-40px}
.hub-name span.dot{width:26px;height:26px;border-radius:50%;background:var(--blue)}
.hub-about{left:0;top:680px;width:1200px;text-align:center;font-family:"Exo 2",sans-serif;font-style:italic;font-weight:500;font-size:30px;color:#666}

/* about */
.about-text{left:88px;top:1368px;width:1024px;text-align:center;font-size:14.5px;line-height:24px;color:#222}
.about-text strong{color:var(--blue)}

/* band */
.strive{left:0;top:1536px;width:1200px;height:145px;background:var(--blue);color:#fff;display:flex;align-items:center;justify-content:center;text-align:center;font-family:"Exo 2",sans-serif;font-style:italic;font-weight:600;font-size:26px;line-height:38px}

/* gallery */
.gallery{left:0;top:1681px;width:1200px;height:614px;background:linear-gradient(#fafafa,#ededee)}
.gallery .section-title span,.testimonials .section-title span,.clients .section-title span{color:#8b9097}
.monitor{left:345px;top:133px;width:510px;height:340px;background:#1b1b1b;border-radius:14px}
.screen{left:368px;top:150px;width:464px;height:290px;background:linear-gradient(#3e6da3,#8fb2cf 55%,#39502e)}
.caption{left:368px;top:330px;width:464px;height:80px;background:rgba(255,255,255,.78);text-align:center;font-family:"Exo 2",sans-serif;font-style:italic;font-weight:600;font-size:26px;color:var(--blue);line-height:34px;padding-top:8px;text-transform:uppercase}
.stand{left:548px;top:473px;width:104px;height:70px;background:linear-gradient(#d9dadc,#9fa2a6)}
.base{left:470px;top:540px;width:260px;height:22px;background:linear-gradient(#e6e7e8,#b8babd);border-radius:50%}
.arrow{width:36px;height:60px;border-right:2px solid #ccc;border-radius:50%}

/* testimonials */
.testimonials{left:0;top:2295px;width:1200px;height:491px;background:var(--dark)}
.testimonials .section-title{color:#fff}
.video{left:79px;top:140px;width:372px;height:220px;background:#cfd0d2;border-radius:6px;padding:10px 8px}
.video-inner{width:100%;height:180px;background:linear-gradient(90deg,#1e1e1e,#5b5148 45%,#1e1e1e)}
.name-tab{left:455px;top:140px;width:325px;height:45px;background:var(--blue);color:#fff;font-family:"Exo 2",sans-serif;font-style:italic;font-weight:600;font-size:19px;line-height:45px;padding-left:14px}
.quote{left:470px;top:198px;width:660px;font-style:italic;font-size:14px;line-height:24px;color:#ddd}
.quote-by{left:470px;top:341px;font-family:"Exo 2",sans-serif;font-style:italic;font-weight:600;font-size:16px;color:#eee}

/* clients */
.clients{left:0;top:2786px;width:1200px;height:172px;background:var(--light)}
.footer{left:0;top:2958px;width:1200px;height:498px;background:var(--blue)}
.client-strip{left:82px;top:2895px;width:1039px;height:94px;background:#fff;border:2px solid var(--blue);display:flex;align-items:center;justify-content:space-around;padding:0 40px}
.client{font-family:"Lato",sans-serif;font-weight:700;font-size:20px;color:#333;display:flex;align-items:center;gap:8px}
.client i{width:14px;height:14px;background:#333;display:block}
.strip-arrow{width:28px;height:28px;border-radius:50%;background:#6d747c;border:2px solid #fff}

/* footer */
.foot-nav{left:0;top:3032px;width:1200px;display:flex;justify-content:center;gap:0;font-family:"Exo 2",sans-serif;font-style:italic;font-weight:600;font-size:15px;color:#fff}
.foot-nav span{padding:0 18px}
.foot-nav span+span::before{content:"•";position:relative;left:-20px;color:#8fb2dc}
.map{left:169px;top:3106px;width:270px;height:270px;border-radius:50%;background:radial-gradient(#e6efe0,#c6d8e8);border:5px solid #cfe0f4}
.map-label{left:224px;top:3165px;width:170px;background:#fff;border:1px solid #999;font-size:13px;line-height:17px;padding:5px 8px;text-align:center;color:var(--blue-deep)}
.form-label{font-size:12px;font-weight:700;color:#fff}
.form-label b{color:#f5a0a0}
.field{background:#fff;height:28px}
.submit{left:957px;top:3381px;width:117px;height:38px;border-radius:19px;background:#7f878f;color:#fff;font-family:"Exo 2",sans-serif;font-style:italic;font-weight:600;font-size:17px;text-align:center;line-height:38px}
.foot-contact{top:3403px;display:flex;align-items:center;gap:10px;color:#fff;font-size:18px}
.bottom-bar{left:0;top:3456px;width:1200px;height:46px;background:var(--blue-deep);color:#ddd;font-family:"Exo 2",sans-serif;font-style:italic;font-size:13px;font-weight:600;line-height:46px;padding-left:82px}
.mini{width:22px;height:22px;border-radius:50%;background:var(--blue);border:1px solid #fff}
</style>
</head>
<body>
<div class="page">

<header class="abs site-header">
  <div class="abs brand"><span class="brand-name">Velmoro</span><span class="brand-dot"></span></div>
  <div class="abs top-contact">
    <svg width="18" height="18" viewBox="0 0 24 24"><path fill="#0b4a92" d="M6.6 10.8a15 15 0 006.6 6.6l2.2-2.2a1 1 0 011-.25 11.4 11.4 0 003.6.57 1 1 0 011 1V20a1 1 0 01-1 1A17 17 0 013 4a1 1 0 011-1h3.5a1 1 0 011 1c0 1.25.2 2.45.57 3.57a1 1 0 01-.25 1z"/></svg>
    <span>1300 555 014</span>
    <span class="social"></span><span class="social"></span>
  </div>
  <nav class="abs main-nav">
    <a class="current">Home</a><a>About Us</a><a>Services</a><a>Work Gallery</a><a>Contact Us</a>
  </nav>
  <div class="abs portal">PORTAL</div>
</header>

<section class="abs hero" role="img" aria-label="Hotel bedroom at night with city view"></section>
<h1 class="abs hero-title">Hospitality Solutions</h1>
<div class="abs hero-btn">Read More</div>
<div class="abs hero-tab" style="top:539px"><i></i><i class="on"></i><i></i><i></i></div>

<section class="abs services">
  <h2 class="abs section-title head" style="top:38px">Our Services</h2>
  <p class="abs services-lead">Lorem ipsum dolor sit amet consectetuer adipiscing elit sed diam nonummy nibh euismod tincidunt</p>

  <div class="abs svc-label" style="left:468px;top:156px">Managed Networks</div>
  <div class="abs svc-icon" style="left:544px;top:200px">
    <svg width="50" height="44" viewBox="0 0 50 44" fill="none" stroke="#fff" stroke-width="5" stroke-linecap="round"><path d="M5 16a28 28 0 0140 0"/><path d="M12 24a18 18 0 0126 0"/><path d="M19 32a8 8 0 0112 0"/><circle cx="25" cy="39" r="2.5" fill="#fff"/></svg>
  </div>

  <div class="abs svc-label" style="left:153px;top:273px">Velmoro TV Solution</div>
  <div class="abs svc-icon" style="left:229px;top:317px">
    <svg width="48" height="42" viewBox="0 0 48 42" fill="none" stroke="#fff" stroke-width="4"><rect x="3" y="3" width="42" height="28" rx="2"/><path d="M16 39h16M24 31v8"/></svg>
  </div>

  <div class="abs svc-label" style="left:783px;top:273px">Mobile Solution</div>
  <div class="abs svc-icon" style="left:859px;top:317px">
    <svg width="30" height="50" viewBox="0 0 30 50" fill="none" stroke="#fff" stroke-width="4"><rect x="3" y="3" width="24" height="44" rx="4"/><circle cx="15" cy="40" r="2" fill="#fff"/></svg>
  </div>

  <div class="abs svc-label active" style="left:92px;top:506px">Hospitality Solutions</div>
  <div class="abs svc-icon active" style="left:168px;top:550px">
    <svg width="40" height="44" viewBox="0 0 40 44" fill="#fff"><path d="M6 4h28v38H24v-8h-8v8H6z"/><g fill="#0b4a92"><rect x="11" y="9" width="5" height="5"/><rect x="18" y="9" width="5" height="5"/><rect x="25" y="9" width="5" height="5"/><rect x="11" y="17" width="5" height="5"/><rect x="18" y="17" width="5" height="5"/><rect x="25" y="17" width="5" height="5"/><rect x="11" y="25" width="5" height="5"/><rect x="25" y="25" width="5" height="5"/></g></svg>
  </div>

  <div class="abs svc-label" style="left:846px;top:506px">Social Wi-Fi</div>
  <div class="abs svc-icon" style="left:922px;top:550px">
    <svg width="46" height="42" viewBox="0 0 46 42" fill="none" stroke="#fff" stroke-width="4" stroke-linejoin="round"><path d="M4 4h38v26H20l-10 8v-8H4z"/></svg>
  </div>

  <div class="abs hub"><div class="hub-name">Velmoro<span class="dot"></span></div></div>
  <div class="abs hub-about">About</div>
</section>

<p class="abs about-text"><strong>Velmoro Wireless</strong> is at the forefront of revolutionising high-speed internet access (HSIA) services. We offer complete wireless solutions: Right from developing individual components such as hotspots and access controllers, to installation of the internet infrastructure. Once we setup the HSIA for our clients, we back it up with round-the-clock tech support.</p>
<div class="btn" style="left:536px;top:1464px;width:128px">Read More</div>

<div class="abs strive">We strive to out work our competition with an effective approach and a powerful skill set,<br>which is why were industry leading.</div>

<section class="abs gallery">
  <h2 class="abs section-title head" style="top:44px">Work <span>Gallery</span></h2>
  <div class="abs monitor"></div>
  <div class="abs screen" role="img" aria-label="Modern apartment building against a blue sky"></div>
  <div class="abs caption">Crestline Harbour Suites<br>Completed August 2013</div>
  <div class="abs stand"></div>
  <div class="abs base"></div>
  <svg class="abs" style="left:228px;top:282px" width="24" height="30" viewBox="0 0 24 30"><path d="M16 5L6 15l10 10" stroke="#111" stroke-width="4" fill="none"/></svg>
  <svg class="abs" style="left:946px;top:282px" width="24" height="30" viewBox="0 0 24 30"><path d="M8 5l10 10-10 10" stroke="#111" stroke-width="4" fill="none"/></svg>
</section>

<section class="abs testimonials">
  <h2 class="abs section-title head" style="top:46px">Video <span>Testimonials</span></h2>
  <div class="abs video"><div class="video-inner" role="img" aria-label="Video still of a client speaking"></div></div>
  <svg class="abs" style="left:232px;top:218px" width="50" height="50" viewBox="0 0 50 50"><circle cx="25" cy="25" r="24" fill="rgba(255,255,255,.75)"/><path d="M20 15l14 10-14 10z" fill="#0b4a92"/></svg>
  <div class="abs name-tab">Owen Hartley - Property Manager</div>
  <p class="abs quote">Installing Velmoro Internet Solution has been a great investment for this business. The staff were very professional and easy to work with and gave us several options to consider that would work best for the business. The installation was easy and happened without any problems at all. The system is easy to use for both guests and staff, which can be tailored to suit the needs of the guest and business, which was a deciding factor. I would highly recommend Velmoro as you're in room internet solution.</p>
  <div class="abs quote-by">Liam Carter - Crestline Ballarat</div>
  <div class="btn" style="left:542px;top:404px;width:116px">View All</div>
</section>

<section class="abs clients">
  <h2 class="abs section-title head" style="top:38px">Our <span style="color:var(--blue)">Clients</span></h2>
</section>
<footer class="abs footer"></footer>
<div class="abs client-strip">
  <span class="client"><i></i>Harbourline</span>
  <span class="client">Pinewell</span>
  <span class="client">Stonegate</span>
  <span class="client">Roamly</span>
  <span class="client">Basecamp</span>
  <span class="client">Coachway</span>
</div>
<div class="abs strip-arrow" style="left:68px;top:2928px"></div>
<div class="abs strip-arrow" style="left:1107px;top:2928px"></div>

<nav class="abs foot-nav">
  <span>Home</span><span>About Us</span><span>Services</span><span>Work Gallery</span><span>Case Studies</span><span>Testimonials</span><span>News</span><span>Resellers</span><span>Contact Us</span>
</nav>

<div class="abs map" role="img" aria-label="Coastal area map with office location"></div>
<div class="abs map-label">42 Harbour Lane<br>Coral Point, QLD 4300</div>
<svg class="abs" style="left:293px;top:3214px" width="22" height="32" viewBox="0 0 22 32"><path d="M11 1a10 10 0 0110 10c0 8-10 20-10 20S1 19 1 11A10 10 0 0111 1z" fill="#d9302c"/><circle cx="11" cy="11" r="4" fill="#fff"/></svg>

<div class="abs form-label" style="left:553px;top:3102px"><b>*</b> Name</div>
<div class="abs form-label" style="left:821px;top:3102px"><b>*</b> Email</div>
<div class="abs field" style="left:553px;top:3128px;width:254px"></div>
<div class="abs field" style="left:821px;top:3128px;width:253px"></div>
<div class="abs form-label" style="left:553px;top:3167px"><b>*</b> Phone</div>
<div class="abs form-label" style="left:821px;top:3167px"><b>*</b> Subject</div>
<div class="abs field" style="left:553px;top:3192px;width:254px"></div>
<div class="abs field" style="left:821px;top:3192px;width:253px"></div>
<div class="abs form-label" style="left:553px;top:3232px">Your Message</div>
<div class="abs field" style="left:553px;top:3255px;width:521px;height:107px"></div>
<div class="abs submit">Submit</div>

<div class="abs foot-contact" style="left:126px">
  <svg width="20" height="20" viewBox="0 0 24 24"><path fill="#fff" d="M6.6 10.8a15 15 0 006.6 6.6l2.2-2.2a1 1 0 011-.25 11.4 11.4 0 003.6.57 1 1 0 011 1V20a1 1 0 01-1 1A17 17 0 013 4a1 1 0 011-1h3.5a1 1 0 011 1c0 1.25.2 2.45.57 3.57a1 1 0 01-.25 1z"/></svg>
  <span>1300 555 014</span>
</div>
<div class="abs foot-contact" style="left:292px">
  <svg width="24" height="18" viewBox="0 0 24 18" fill="none" stroke="#fff" stroke-width="2"><rect x="1" y="1" width="22" height="16"/><path d="M1 1l11 9 11-9"/></svg>
  <span>sales@velmoro.com.au</span>
</div>

<div class="abs bottom-bar">© 2015 Velmoro wireless internet. All Rights Reserved.</div>
<div class="abs mini" style="left:1059px;top:3468px"></div>
<div class="abs mini" style="left:1085px;top:3468px"></div>
<svg class="abs" style="left:1128px;top:3468px" width="22" height="22" viewBox="0 0 22 22"><circle cx="11" cy="11" r="10" fill="none" stroke="#ccc" stroke-width="1.5"/><path d="M6 13l5-5 5 5" fill="none" stroke="#ccc" stroke-width="2"/></svg>

</div>
</body>
</html>
```